bottle label design for a cultured milk based product

(Edit : name of the company is Qeshari . The bottle will be see through )
Edit 2 :I noticed people only sending a logo this isn't what I want please read the description

I'm starting a small dairy company for cultured milk products .

1. I need a logo
2.i need a design for the bottle label
3. I need a design for the bottle it's self

As a professional suggest for me the sizes for large medium and small (ie 1.5 liter) .

We are still brainstorming this but hope you can help us how it will be designed

The main theme behind it is as follows
Camel based milk
Cultured/fermented/probiotic milk
Fenugreek added to enhance flavour
Organic
Plant based biodegradable bottle (eco-friendly)
(Shake before use)

This must be a full label which also includes the nutritional break down table but keep it empty for us to fill in

Since on the bigger bottles has more space and I thought we could add a small story since cultured milk is part of our history (united Arab Emirates)

The idea of how the label would look like is that it can have a small outline of a camel and a brown background of sand dunes and the font would be in white but you can ignore all of this and show us what you can think of

If we have missed something , as a professional guide us .

```html
<!DOCTYPE html>
<html lang="en">
<head>
<meta charset="utf-8">
<title>Qeshari Organic – Fermented Camel Milk Label Set</title>
<link rel="stylesheet" href="https://fonts.googleapis.com/css2?family=Poppins:wght@400;500;600;700&family=Lora:wght@400;500&family=Noto+Naskh+Arabic:wght@500&display=swap">
<style>
  :root {
    --bg: #a8dfe0;
    --label: #f6f8f8;
    --ink: #2f3030;
    --ink-soft: #6d7070;
    --orange: #c97a3a;
    --sand-light: #f1e6cf;
    --sand: #d9b97e;
    --sand-dark: #a88650;
    --rule: #d6d9d9;
  }
  * { box-sizing: border-box; margin: 0; padding: 0; }
  html, body { width: 1200px; height: 900px; overflow: hidden; }
  body {
    background: var(--bg);
    font-family: "Poppins", sans-serif;
    color: var(--ink);
    position: relative;
  }
  .label {
    position: absolute;
    background: var(--label);
    box-shadow: 0 6px 18px rgba(0,0,0,0.08);
  }

  /* ---------- side strip label ---------- */
  .strip { left: 190px; top: 225px; width: 80px; height: 440px; }
  .strip-inner {
    position: absolute; top: 0; left: 0;
    width: 440px; height: 80px;
    transform-origin: top left;
    transform: translateX(80px) rotate(90deg);
    display: flex; padding: 8px 10px;
  }
  .strip-brand { width: 140px; display: flex; flex-direction: column; justify-content: center; }
  .strip-brand .name { font-size: 23px; font-weight: 600; letter-spacing: 2px; line-height: 1; }
  .strip-brand .organic {
    display: flex; align-items: center; gap: 4px;
    font-size: 9px; letter-spacing: 4px; color: var(--orange); margin-top: 3px;
  }
  .strip-brand .organic::before, .strip-brand .organic::after {
    content: ""; flex: 1; height: 1.5px; background: var(--orange);
  }
  .strip-brand .serving { font-size: 9px; margin-top: 6px; letter-spacing: 0.5px; }
  .strip-table {
    flex: 1; border-collapse: collapse; font-size: 8px;
    border: 1px solid var(--orange);
  }
  .strip-table td { border: 1px solid var(--orange); padding: 2px 5px; vertical-align: top; }
  .strip-table .head td { font-size: 11px; font-weight: 600; height: 24px; vertical-align: middle; }
  .strip-table .lines { line-height: 1.15; }

  /* ---------- story label ---------- */
  .story { left: 300px; top: 225px; width: 200px; height: 440px; padding: 48px 16px 20px; }
  .story h2 { font-family: "Lora", serif; font-weight: 400; font-size: 24px; letter-spacing: 1px; line-height: 1.1; }
  .story h3 { font-family: "Lora", serif; font-weight: 400; font-size: 11px; letter-spacing: 1px; margin: 4px 0 0 36px; }
  .story .rule { height: 1.5px; background: var(--orange); margin: 5px 0 20px 36px; }
  .story p { font-size: 9.5px; line-height: 1.5; color: var(--ink-soft); margin-bottom: 16px; }
  .story .arabic { font-family: "Noto Naskh Arabic", serif; font-size: 15px; text-align: center; direction: rtl; margin-top: 26px; color: var(--ink); }

  /* ---------- front label ---------- */
  .front { left: 530px; top: 210px; width: 230px; height: 470px; padding-top: 64px; text-align: center; overflow: hidden; }
  .front .brand { font-size: 38px; font-weight: 600; letter-spacing: 2px; line-height: 1; }
  .front .organic {
    display: flex; align-items: center; gap: 8px;
    width: 168px; margin: 4px auto 0;
    font-size: 12px; letter-spacing: 6px; color: var(--orange);
  }
  .front .organic::before, .front .organic::after { content: ""; flex: 1; height: 2px; background: var(--orange); }
  .front .kind { font-size: 12px; font-weight: 600; letter-spacing: 1px; margin-top: 22px; }
  .front .product { font-size: 28px; font-weight: 600; letter-spacing: 1px; line-height: 1.1; }
  .front .flavour { font-family: "Lora", serif; font-size: 11px; letter-spacing: 2px; }
  .front .scene {
    position: absolute; left: 0; right: 0; top: 255px; height: 180px;
    background: linear-gradient(180deg, var(--label) 0%, var(--sand-light) 45%, var(--sand) 75%, var(--sand-dark) 100%);
  }
  .front .volume {
    position: absolute; left: 50%; bottom: 10px; transform: translateX(-50%);
    background: var(--orange); color: #fff; font-size: 12px; font-weight: 500;
    padding: 2px 12px; letter-spacing: 1px;
  }

  /* ---------- nutrition label ---------- */
  .nutrition { left: 790px; top: 330px; width: 220px; height: 325px; padding: 12px 12px 10px; }
  .nutrition .top { display: flex; justify-content: space-between; border: 1px solid var(--ink); padding: 6px 8px; }
  .nutrition h4 { font-size: 18px; font-weight: 600; line-height: 1.05; }
  .nutrition .intro { font-size: 7px; margin-top: 6px; color: var(--ink-soft); }
  .nutrition .intro b { display: block; color: var(--ink); font-weight: 600; }
  .nutrition .cert { width: 46px; height: 34px; border: 1.5px solid var(--ink); border-radius: 4px; align-self: center; }
  .nutrition table { width: 100%; border-collapse: collapse; font-size: 7px; margin-top: 8px; }
  .nutrition td { padding: 3px 0; border-bottom: 1px solid var(--rule); }
  .nutrition td.val { text-align: right; }
  .nutrition .cal td { font-size: 10px; font-weight: 600; border-bottom: 3px solid var(--ink); }
  .nutrition .cal small { display: block; font-size: 5px; font-weight: 400; color: var(--ink-soft); }
  .nutrition .main td:first-child { font-weight: 600; }
  .nutrition .sub td:first-child { padding-left: 10px; }
  .nutrition .foot { display: flex; align-items: center; justify-content: space-between; margin-top: 8px; }
  .nutrition .foot p { font-size: 6px; color: var(--ink-soft); width: 70px; line-height: 1.3; }
  .nutrition .badges { display: flex; gap: 6px; }
  .nutrition .badge { width: 18px; height: 18px; border: 1px solid var(--ink); border-radius: 50%; }
</style>
</head>
<body>

  <section class="label strip" aria-label="Side label">
    <div class="strip-inner">
      <div class="strip-brand">
        <div class="name">QESHARI</div>
        <div class="organic">ORGANIC</div>
        <div class="serving">6 Serving per container</div>
      </div>
      <table class="strip-table">
        <tr class="head"><td>Calories</td><td>12mg</td><td>8mg</td><td>14mg</td></tr>
        <tr>
          <td class="lines">Total Fat<br>Saturates<br>Trans Flat<br>Salt</td>
          <td class="lines">210mg<br>12mg<br>134mg<br>0.34mg</td>
          <td class="lines">210mg<br>12mg<br>134mg<br>0.34mg</td>
          <td class="lines">210mg<br>12mg<br>134mg<br>0.34mg</td>
        </tr>
      </table>
    </div>
  </section>

  <section class="label story" aria-label="Back label with brand story">
    <h2>OUR HISTORY</h2>
    <h3>OF CULTURED MILK</h3>
    <div class="rule"></div>
    <p>Qeshari Camel Milk dummy text of the printing and typesetting industry. Lorem Ipsum has been the industry's standard dummy text.</p>
    <p>Since the 1500s, when an unknown printer took a galley of type and scrambled it to make a type specimen book. It has survived not only.</p>
    <p class="arabic">الإمارات العربية المتحدة</p>
  </section>

  <section class="label front" aria-label="Front label">
    <div class="brand">QESHARI</div>
    <div class="organic">ORGANIC</div>
    <div class="kind">FARMENTED</div>
    <div class="product">CAMEL MILK</div>
    <div class="flavour">WITH FENUGREEK</div>
    <div class="scene" role="img" aria-label="Illustration of a camel under a rising sun over desert sand dunes"></div>
    <div class="volume">1.5 L</div>
  </section>

  <section class="label nutrition" aria-label="Nutrition facts label">
    <div class="top">
      <div>
        <h4>Nutrition<br>Facts</h4>
        <p class="intro">Qeshari Contain High <b>Calcium</b></p>
      </div>
      <div class="cert" role="img" aria-label="Certification badge"></div>
    </div>
    <table>
      <tr class="cal"><td>Calories</td><td class="val"><small>Per serving</small>245</td><td class="val"><small>Per container</small>490</td></tr>
      <tr class="main"><td colspan="2">Total Fat</td><td class="val">217 mg</td></tr>
      <tr class="sub"><td colspan="2">Saturates</td><td class="val">11 mg</td></tr>
      <tr class="sub"><td colspan="2">Trans Flat</td><td class="val">21 mg</td></tr>
      <tr class="sub"><td colspan="2">Salt</td><td class="val">21 mg</td></tr>
      <tr class="main"><td colspan="2">Cholesterol</td><td class="val">128 mg</td></tr>
      <tr class="main"><td colspan="2">Sodium</td><td class="val">34mg</td></tr>
      <tr class="main"><td colspan="2">Protein</td><td class="val">56 mg</td></tr>
      <tr class="main"><td colspan="2">Vitamins</td><td class="val">41 mg</td></tr>
      <tr class="sub"><td colspan="2">Vitamin A 12mg</td><td class="val">21 mg</td></tr>
      <tr class="sub"><td colspan="2">Vitamin B 17mg</td><td class="val">21 mg</td></tr>
    </table>
    <div class="foot">
      <p>Qeshari keep chilled, shake well</p>
      <div class="badges">
        <span class="badge" role="img" aria-label="Organic badge"></span>
        <span class="badge" role="img" aria-label="Eco badge"></span>
        <span class="badge" role="img" aria-label="Recyclable badge"></span>
      </div>
    </div>
  </section>

</body>
</html>
```